Harborline Deed Partners Stationery
HDP Stationery
Harborline Deed Partners Stationery - Real Estate
Creative Brief
Professional
Leopoldo Marvinez II
Manager
4817 North Palmetto Lane, Suite 320 Coconut Grove, Florida 33129
lm@harborlinedeedpartners.example
www.harborlinedeedpartners.example
$100 bonus to winning designer upon designer creating duplicate design and stationery for "Harborline Deed Alliance"

```html
<!DOCTYPE html>
<html lang="en">
<head>
<meta charset="utf-8">
<title>Harborline Deed Partners – Business Card</title>
<link href="https://fonts.googleapis.com/css2?family=Open+Sans:wght@400;600;700;800&display=swap" rel="stylesheet">
<style>
  :root {
    --stage: #e4e0da;
    --card-dark: #26282e;
    --card-dark-2: #1c1d22;
    --card-light: #f1f1f0;
    --ink: #26282e;
    --ink-soft: #6d6f73;
    --green: #3f9e2f;
    --green-deep: #2f7f22;
    --rule: #8a8c90;
    --white: #ffffff;
  }
  * { box-sizing: border-box; margin: 0; padding: 0; }
  html, body { width: 1200px; height: 795px; overflow: hidden; }
  body {
    background: var(--stage);
    font-family: "Open Sans", Arial, sans-serif;
    position: relative;
  }
  .card {
    position: absolute;
    top: 243px;
    width: 540px;
    height: 309px;
    border-radius: 22px;
    overflow: hidden;
    box-shadow: 0 10px 28px rgba(0,0,0,.22);
  }

  /* Front */
  .card-front {
    left: 40px;
    background: linear-gradient(135deg, #3a3d44 0%, var(--card-dark) 45%, var(--card-dark-2) 100%);
    color: var(--white);
  }
  .front-accent {
    position: absolute; right: 0; top: 0;
    width: 190px; height: 150px;
    background: linear-gradient(225deg, rgba(63,158,47,.35), rgba(63,158,47,0) 70%);
  }
  .front-brand {
    position: absolute; left: 96px; top: 104px;
    display: flex; align-items: center; gap: 18px;
  }
  .brand-square {
    width: 46px; height: 46px; background: var(--green); flex: none;
  }
  .brand-divider { width: 1px; height: 74px; background: var(--rule); }
  .wordmark-title {
    font-weight: 800; font-size: 34px; letter-spacing: .5px; line-height: 1;
    text-transform: uppercase;
  }
  .wordmark-sub {
    display: flex; align-items: center; gap: 10px; margin-top: 6px;
    font-size: 15px; letter-spacing: 5px; text-transform: uppercase; font-weight: 400;
  }
  .wordmark-sub .line { height: 1px; flex: 1; background: var(--rule); }
  .front-web {
    position: absolute; left: 0; right: 0; top: 212px;
    text-align: center; font-size: 15px; color: #e8e8e8;
  }

  /* Back */
  .card-back { left: 620px; background: var(--card-light); color: var(--ink); }
  .back-brand {
    position: absolute; left: 30px; top: 58px;
    display: flex; align-items: center; gap: 14px;
  }
  .back-brand .brand-square { width: 40px; height: 40px; }
  .back-brand .brand-divider { height: 62px; }
  .back-brand .wordmark-title { font-size: 27px; color: var(--ink); }
  .back-brand .wordmark-sub { font-size: 12px; letter-spacing: 4px; color: var(--ink); }
  .back-rule { position: absolute; left: 40px; top: 150px; width: 470px; height: 1px; background: var(--rule); }
  .person { position: absolute; right: 28px; top: 108px; text-align: right; }
  .person-name { font-weight: 700; font-size: 19px; color: var(--ink); }
  .person-role { position: absolute; right: 28px; top: 156px; font-size: 12px; color: var(--ink-soft); }
  .contacts {
    position: absolute; left: 40px; top: 170px;
    list-style: none; font-size: 12.5px; line-height: 19px; color: var(--ink);
  }
  .contacts li { display: flex; align-items: center; gap: 8px; }
  .contacts svg { width: 13px; height: 13px; flex: none; }
  .address {
    position: absolute; right: 24px; top: 206px; text-align: right;
    font-size: 12px; line-height: 16px; color: var(--ink);
  }
  .back-band { position: absolute; left: 0; bottom: 0; width: 540px; height: 44px; }
  .back-web {
    position: absolute; right: 24px; bottom: 13px;
    font-size: 12px; color: #e8e8e8;
  }
</style>
</head>
<body>

<section class="card card-front" aria-label="Business card front">
  <div class="front-accent"></div>
  <div class="front-brand">
    <div class="brand-square"></div>
    <div class="brand-divider"></div>
    <div class="wordmark">
      <div class="wordmark-title">Harborline Deed</div>
      <div class="wordmark-sub"><span class="line"></span>Partners<span class="line"></span></div>
    </div>
  </div>
  <p class="front-web">www.harborlinedeedpartners.example</p>
</section>

<section class="card card-back" aria-label="Business card back">
  <div class="back-brand">
    <div class="brand-square"></div>
    <div class="brand-divider"></div>
    <div class="wordmark">
      <div class="wordmark-title">Harborline Deed</div>
      <div class="wordmark-sub"><span class="line"></span>Partners<span class="line"></span></div>
    </div>
  </div>

  <div class="person"><p class="person-name">Leopoldo Marvinez II</p></div>
  <div class="back-rule"></div>
  <p class="person-role">Manager</p>

  <ul class="contacts">
    <li><svg viewBox="0 0 14 14"><circle cx="7" cy="7" r="7" fill="#3f9e2f"/><path d="M4.5 3.8l1.4-.3.7 1.7-.8.6a4.5 4.5 0 0 0 2.4 2.4l.6-.8 1.7.7-.3 1.4c-3 .2-5.9-2.7-5.7-5.7z" fill="#fff"/></svg>305-555-0142</li>
    <li><svg viewBox="0 0 14 14"><circle cx="7" cy="7" r="7" fill="#3f9e2f"/><rect x="5" y="3.3" width="4" height="7.4" rx=".8" fill="#fff"/></svg>305-555-0187</li>
    <li><svg viewBox="0 0 14 14"><circle cx="7" cy="7" r="7" fill="#3f9e2f"/><rect x="3.8" y="5.5" width="6.4" height="4.2" fill="#fff"/><rect x="5" y="3.5" width="4" height="2" fill="#fff"/></svg>305-555-0163</li>
    <li><svg viewBox="0 0 14 14"><circle cx="7" cy="7" r="7" fill="#3f9e2f"/><rect x="3.6" y="4.6" width="6.8" height="4.8" fill="#fff"/><path d="M3.6 4.6L7 7.4l3.4-2.8" fill="none" stroke="#3f9e2f" stroke-width=".8"/></svg>lm@harborlinedeedpartners.example</li>
  </ul>

  <p class="address">4817 North Palmetto Lane, Suite 320<br>Coconut Grove, Florida 33129</p>

  <svg class="back-band" viewBox="0 0 540 44" preserveAspectRatio="none" aria-hidden="true">
    <polygon points="0,44 0,30 300,30 318,0 540,0 540,44" fill="#26282e"/>
    <polygon points="0,44 0,30 300,30 318,0 330,0 316,44" fill="#3f9e2f"/>
    <polygon points="0,44 0,34 290,34 302,44" fill="#2f7f22"/>
  </svg>
  <p class="back-web">www.harborlinedeedpartners.example</p>
</section>

</body>
</html>
```